I need a SEO-friendly Wordpress website (making sure to style H1, H2, H3, etc correctly) for a Hawaii-based law firm called Meridale Crown Legal Group. Comparable websites include https://brvtlaw.com/ and https://www.lorvin.com/ for design reference. The current copy on the TuvellAttorney.com website can be used.

Coding

Coded - Design and coding required

```html
<!DOCTYPE html>
<html lang="en">
<head>
<meta charset="utf-8">
<title>Meridale Crown Legal Group – Divorce and Personal Injury Lawyers</title>
<link rel="stylesheet" href="https://fonts.googleapis.com/css2?family=Open+Sans:wght@400;600;700&display=swap">
<style>
:root{
  --orange:#d2711f;
  --orange-dark:#a9560f;
  --ink:#1d1d1d;
  --body:#555;
  --nav:#6b6b6b;
  --light:#efefef;
  --footer:#2c2c2c;
  --white:#fff;
}
*{box-sizing:border-box;margin:0;padding:0}
html,body{width:711px;height:1200px;overflow:hidden}
body{position:relative;font-family:"Open Sans",sans-serif;color:var(--ink);background:var(--white)}
.abs{position:absolute}

/* header */
.site-header{position:absolute;left:0;top:0;width:711px;height:82px;border-top:2px solid var(--orange)}
.phone-tab{position:absolute;left:549px;top:0;width:104px;height:17px;background:var(--orange);color:var(--white);font-size:8.5px;font-weight:600;display:flex;align-items:center;justify-content:center;gap:5px;clip-path:polygon(0 0,100% 0,100% 100%,9px 100%)}
.phone-tab svg{width:8px;height:8px}
.brand{position:absolute;left:57px;top:25px}
.brand-name{font-size:15.5px;font-weight:400;color:var(--orange);letter-spacing:.4px;text-transform:uppercase;padding-bottom:3px;border-bottom:1px solid var(--orange)}
.brand-tag{font-size:8.5px;color:var(--orange);letter-spacing:1.6px;margin-top:3px}
.main-nav{position:absolute;top:29px;right:58px;display:flex;gap:0}
.main-nav a{display:flex;flex-direction:column;align-items:center;text-decoration:none;color:var(--nav);font-size:7.5px;letter-spacing:.2px;margin-left:21px}
.main-nav a svg{width:17px;height:17px;margin-bottom:6px}
.main-nav a.is-current{color:var(--orange)}

/* hero */
.hero{position:absolute;left:0;top:82px;width:711px;height:237px;background:linear-gradient(90deg,#3b3a38 0%,#2a2826 45%,#24211f 100%)}
.hero-photo{position:absolute;left:0;top:0;width:300px;height:237px;background:radial-gradient(ellipse at 40% 45%,#8a5b33 0%,#5d3d24 35%,#6b6b6b 65%,rgba(43,41,39,0) 100%)}
.hero-copy{position:absolute;left:464px;top:24px;width:220px;color:var(--white);font-size:12px;font-weight:600;line-height:15.2px;text-transform:uppercase}
.hero-copy p{margin-bottom:11px}
.hero-copy .hl{color:var(--orange);display:block}

/* about */
.about{position:absolute;left:0;top:319px;width:711px;height:223px;background:var(--light)}
.about h2{position:absolute;left:57px;top:28px;font-size:12px;font-weight:400;text-transform:uppercase}
.about-text{position:absolute;left:57px;top:50px;width:358px;font-size:7.4px;line-height:13.2px;color:var(--body)}
.about-text p+p{margin-top:13px}
.btn{position:absolute;left:57px;top:166px;width:66px;height:21px;background:var(--orange);border-bottom:2px solid var(--orange-dark);border-radius:2px;color:var(--white);font-size:7.2px;font-weight:600;display:flex;align-items:center;justify-content:center;text-decoration:none}
.about-frame{position:absolute;left:479px;top:31px;width:127px;height:115px;border:1px solid var(--orange)}
.about-photo{position:absolute;left:490px;top:41px;width:163px;height:151px;background:linear-gradient(135deg,#7a4a24 0%,#a06a35 40%,#5a3418 75%,#3a2010 100%)}

/* practices */
.practices{position:absolute;left:0;top:542px;width:711px;height:419px}
.practices h2{position:absolute;left:0;top:28px;width:711px;text-align:center;font-size:12px;font-weight:400;line-height:15.5px;text-transform:uppercase}
.tile{position:absolute;width:188px;height:123px}
.tile-label{position:absolute;width:188px;text-align:center;font-size:11px;text-transform:uppercase}
.ph-family{background:linear-gradient(135deg,#d9d4cc,#b8a99a 60%,#8a7766)}
.ph-injury{background:linear-gradient(135deg,#e3ecec,#9ec6c8 55%,#6fa7aa)}
.ph-ip{background:linear-gradient(135deg,#c9b9a4,#7b4a2c 55%,#4a2a17)}
.ph-estate{background:linear-gradient(135deg,#b6afa7,#8f8780 50%,#5e4a3d)}
.ph-custody{background:linear-gradient(135deg,#a8a49e,#e7e0d4 50%,#6f6a63)}
.ph-team{background:linear-gradient(135deg,#7f8a90,#2d3033 55%,#1b1d1f)}

/* footer */
.site-footer{position:absolute;left:0;top:961px;width:711px;height:207px;background:var(--footer);color:var(--white)}
.footer-col{position:absolute;top:26px}
.footer-col h3{font-size:9px;font-weight:700;text-transform:uppercase;padding-bottom:6px;position:relative}
.footer-col h3::after{content:"";position:absolute;left:0;bottom:-3px;width:31px;height:2px;background:var(--orange)}
.contact-list{list-style:none;margin-top:18px;font-size:7px;line-height:12px}
.contact-list li{display:flex;gap:6px;margin-bottom:12px}
.contact-list svg{width:8px;height:9px;flex:none;margin-top:1px}
.map{position:absolute;left:0;top:25px;width:209px;height:121px;background:linear-gradient(160deg,#f1f1f1,#e6e6e6)}
.sitemap{list-style:none;margin-top:15px}
.sitemap li{font-size:7px;font-weight:600;margin-bottom:12px;text-transform:uppercase}
.copyright{position:absolute;left:0;top:1168px;width:711px;height:32px;background:var(--orange);color:var(--white);font-size:7px;padding-left:58px;display:flex;align-items:center}
</style>
</head>
<body>

<header class="site-header">
  <div class="phone-tab">
    <svg viewBox="0 0 10 10"><path fill="#fff" d="M2 .5l1.6 2-.8 1.1c.6 1.3 1.5 2.2 2.8 2.8l1.1-.8 2 1.6-.9 1.6C4.6 8.9 1 5.4.5 1.4z"/></svg>
    +1.808.555.0142
  </div>
  <div class="brand">
    <div class="brand-name">Meridale Crown Legal Group</div>
    <div class="brand-tag">DIVORCE AND PERSONAL INJURY LAWYERS</div>
  </div>
  <nav class="main-nav">
    <a href="#" class="is-current"><svg viewBox="0 0 20 20"><path fill="#d2711f" d="M10 2L1 10h2.5v8h5v-5h3v5h5v-8H19z"/></svg>HOME</a>
    <a href="#"><svg viewBox="0 0 20 20"><path fill="none" stroke="#888" stroke-width="1.3" d="M5 2h7l4 4v12H5z M12 2v4h4 M8 14l5-5"/></svg>PRACTICE AREAS</a>
    <a href="#"><svg viewBox="0 0 20 20"><g fill="#888"><circle cx="5" cy="7" r="2.3"/><circle cx="10" cy="6" r="2.6"/><circle cx="15" cy="7" r="2.3"/><path d="M1 14c0-3 8-3 8 0zM5 15c0-4 10-4 10 0zM11 14c0-3 8-3 8 0z"/></g></svg>ATTORNEYS</a>
    <a href="#"><svg viewBox="0 0 20 20"><path fill="none" stroke="#888" stroke-width="1.3" d="M3 3h14v11H8l-4 3v-3H3z M6 7h8 M6 10h8"/></svg>BLOG</a>
    <a href="#"><svg viewBox="0 0 20 20"><path fill="none" stroke="#888" stroke-width="1.3" d="M2 5h16v11H2z M2 5l8 6 8-6"/></svg>CONTACT US</a>
  </nav>
</header>

<section class="hero">
  <div class="hero-photo" role="img" aria-label="Wooden gavel and brass scales of justice on a dark desk"></div>
  <div class="hero-copy">
    <h1 style="font-size:inherit;font-weight:inherit"><p>Kona lawyers of MCLG -<br>legal kōkua with aloha.</p></h1>
    <p>Over 70 years of combined practice, specializing in:
      <span class="hl">• Personal injury</span>
      <span class="hl">• Family &amp; divorce</span>
      <span class="hl">• Child custody</span></p>
    <p>Dedicated to making sure you receive the care and attention you need.</p>
  </div>
</section>

<section class="about">
  <h2>About the Kona lawyers of MCLG</h2>
  <div class="about-text">
    <p>The experienced attorneys in the Meridale Crown Legal Group's Kailua Kona, Hawaii office provide clients with a wide range of litigation expertise, including legal claims involving divorce &amp; family, personal injury, toxic exposures, intellectual property, and real estate.</p>
    <p>Our Kona office also offers commercial and hospitality litigation expertise on behalf of a wide variety of clients, including restaurants, hotels, property owners, and many others. We never wish to see our clients go to court, though if there is no other option, you're in safe hands with our seasoned trial lawyers and the many years of courtroom experience behind them.</p>
  </div>
  <a href="#" class="btn">LEARN MORE</a>
  <div class="about-frame"></div>
  <div class="about-photo" role="img" aria-label="Bronze scales of justice on a courtroom table"></div>
</section>

<section class="practices">
  <h2>Over 70 years of combined practice,<br>specializing in:</h2>
  <div class="tile ph-family" style="left:58px;top:74px" role="img" aria-label="Parents arguing behind an upset child"></div>
  <h3 class="tile-label" style="left:55px;top:208px;font-weight:400">Family &amp; Divorce</h3>
  <div class="tile ph-injury" style="left:261px;top:74px" role="img" aria-label="Man fallen on a wet floor holding his back"></div>
  <h3 class="tile-label" style="left:261px;top:208px;font-weight:400">Personal Injury</h3>
  <div class="tile ph-ip" style="left:464px;top:74px" role="img" aria-label="Gavel resting on an intellectual property law book"></div>
  <h3 class="tile-label" style="left:470px;top:208px;font-weight:400">Intellectual Property</h3>
  <div class="tile ph-estate" style="left:60px;top:235px" role="img" aria-label="Model house beside a wooden gavel"></div>
  <h3 class="tile-label" style="left:57px;top:369px;font-weight:400">Real Estate</h3>
  <div class="tile ph-custody" style="left:263px;top:235px" role="img" aria-label="Mother hugging her daughter"></div>
  <h3 class="tile-label" style="left:263px;top:369px;font-weight:400">Child Custody</h3>
  <div class="tile ph-team" style="left:464px;top:235px" role="img" aria-label="Attorneys meeting around a glass table"></div>
  <h3 class="tile-label" style="left:464px;top:369px;font-weight:400">Attorneys</h3>
</section>

<footer class="site-footer">
  <div class="footer-col" style="left:59px">
    <h3>Contact Details</h3>
    <ul class="contact-list">
      <li><svg viewBox="0 0 10 10"><path fill="#d2711f" d="M2 .5l1.6 2-.8 1.1c.6 1.3 1.5 2.2 2.8 2.8l1.1-.8 2 1.6-.9 1.6C4.6 8.9 1 5.4.5 1.4z"/></svg>+1.808.555.0142</li>
      <li><svg viewBox="0 0 10 12"><path fill="#d2711f" d="M5 0a4 4 0 0 1 4 4c0 3-4 8-4 8S1 7 1 4a4 4 0 0 1 4-4zm0 2.3a1.7 1.7 0 1 0 0 3.4 1.7 1.7 0 0 0 0-3.4z"/></svg><span>48-210 Lanakila Avenue, Suite 300<br>Kailua Kona, Hawaii 96799</span></li>
      <li><svg viewBox="0 0 10 8"><path fill="#d2711f" d="M0 0h10v8H0z"/><path fill="none" stroke="#2c2c2c" stroke-width=".8" d="M0 0l5 4 5-4"/></svg>clients@tuvellattorney.com</li>
    </ul>
  </div>
  <div class="footer-col" style="left:262px;width:209px">
    <h3>Find Us Here</h3>
    <div class="map" role="img" aria-label="Street map showing the office location"></div>
  </div>
  <div class="footer-col" style="left:595px">
    <h3>Site Map</h3>
    <ul class="sitemap">
      <li>Home</li><li>Practice Areas</li><li>Attorneys</li><li>Blog</li><li>Contact Us</li>
    </ul>
  </div>
</footer>
<div class="copyright">COPYRIGHT © MERIDALE CROWN LEGAL GROUP. ALL RIGHTS RESERVED.</div>

</body>
</html>
```